we need a business card in yellow, green and black with rounded edges. We are in the Construction and Engineering business. I need the below info included:

Neil Barton
Bluestone Engineering & Construction, Inc.
4168 Harbor Crest Road,
Santa Ana, Ca 92814
714-555-0147 Office
714-555-0192 Cell
714-555-0163 Fax
nb@bluestonexq.example

thanks for your help!

```html
<!DOCTYPE html>
<html lang="en">
<head>
<meta charset="utf-8">
<title>Bluestone Engineering & Construction – Business Card</title>
<link href="https://fonts.googleapis.com/css2?family=Michroma&family=Questrial&display=swap" rel="stylesheet">
<style>
  :root {
    --page: #eceeee;
    --ink: #141414;
    --green: #3fae49;
    --card-light: #f4f4f4;
    --card-mid: #d9d9d9;
    --card-dark: #161616;
    --text-light: #ffffff;
    --watermark: #3a3a3a;
  }
  * { box-sizing: border-box; margin: 0; padding: 0; }
  html, body { width: 960px; height: 1200px; overflow: hidden; }
  body { background: var(--page); position: relative; font-family: "Questrial", sans-serif; }

  .brand {
    display: flex; align-items: center; gap: 18px;
    font-family: "Michroma", sans-serif; color: var(--ink); white-space: nowrap;
  }
  .brand-mark { background: var(--green); flex: none; }
  .brand-name { display: flex; flex-direction: column; line-height: 1; }
  .brand-name .word { letter-spacing: 0.06em; }
  .brand-name .tagline { letter-spacing: 0.12em; margin-top: 10px; }

  .lockup {
    position: absolute; left: 0; top: 0; width: 960px; height: 350px;
    display: flex; justify-content: center; align-items: center;
  }
  .lockup .brand-mark { width: 60px; height: 60px; }
  .lockup .word { font-size: 58px; }
  .lockup .tagline { font-size: 15px; }

  .card {
    position: absolute; left: 162px; width: 672px; height: 386px;
    border-radius: 16px; overflow: hidden;
    box-shadow: 0 4px 14px rgba(0,0,0,0.25);
  }
  .card-front {
    top: 368px;
    background: radial-gradient(ellipse at 50% 45%, #ffffff 0%, var(--card-light) 45%, var(--card-mid) 100%);
    display: flex; justify-content: center; align-items: center;
  }
  .card-front .brand-mark { width: 50px; height: 50px; }
  .card-front .word { font-size: 48px; }
  .card-front .tagline { font-size: 12px; }

  .card-back { top: 776px; background: var(--card-dark); }
  .back-header {
    height: 118px; padding: 0 22px;
    background: linear-gradient(180deg, #ffffff 0%, #efefef 70%, #d4d4d4 100%);
    display: flex; align-items: center;
  }
  .back-header .brand-mark { width: 40px; height: 40px; }
  .back-header .word { font-size: 44px; }
  .back-header .tagline { font-size: 12px; margin-top: 8px; }

  .holder {
    position: absolute; left: 34px; top: 138px;
    color: var(--text-light); font-size: 27px;
  }
  .contact { position: absolute; color: var(--text-light); font-size: 20px; line-height: 1.5; list-style: none; }
  .contact li { display: flex; align-items: flex-start; gap: 10px; }
  .contact svg { flex: none; margin-top: 5px; fill: var(--text-light); }
  .contact-address { left: 44px; top: 196px; }
  .contact-address .email { margin-top: 0; }
  .contact-phones { left: 432px; top: 196px; }

  .watermark {
    position: absolute; right: 22px; bottom: 18px;
    font-family: "Michroma", sans-serif; color: var(--watermark);
    display: flex; flex-direction: column; align-items: flex-end; line-height: 1;
  }
  .watermark .word { font-size: 40px; letter-spacing: 0.06em; }
  .watermark .tagline { font-size: 11px; letter-spacing: 0.14em; margin-top: 6px; }
</style>
</head>
<body>

  <header class="lockup">
    <div class="brand">
      <span class="brand-mark"></span>
      <div class="brand-name"><span class="word">BLUESTONE</span><span class="tagline">ENGINEERING &amp; CONSTRUCTION INC.</span></div>
    </div>
  </header>

  <section class="card card-front">
    <div class="brand">
      <span class="brand-mark"></span>
      <div class="brand-name"><span class="word">BLUESTONE</span><span class="tagline">ENGINEERING &amp; CONSTRUCTION INC.</span></div>
    </div>
  </section>

  <section class="card card-back">
    <div class="back-header">
      <div class="brand">
        <span class="brand-mark"></span>
        <div class="brand-name"><span class="word">BLUESTONE</span><span class="tagline">ENGINEERING &amp; CONSTRUCTION INC.</span></div>
      </div>
    </div>

    <p class="holder">Neil Barton</p>

    <ul class="contact contact-address">
      <li>
        <svg width="16" height="22" viewBox="0 0 16 22"><path d="M8 0a8 8 0 0 0-8 8c0 6 8 14 8 14s8-8 8-14a8 8 0 0 0-8-8zm0 11a3 3 0 1 1 0-6 3 3 0 0 1 0 6z"/></svg>
        <span>4168 Harbor Crest Road,<br>Santa Ana, Ca 92814</span>
      </li>
      <li class="email">
        <svg width="22" height="16" viewBox="0 0 22 16"><path d="M0 0h22v16H0z M1.5 1.5 11 9l9.5-7.5" fill="var(--text-light)"/><path d="M1 1l10 8 10-8" fill="none" stroke="#161616" stroke-width="1.6"/></svg>
        <span>nb@bluestonexq.example</span>
      </li>
    </ul>

    <ul class="contact contact-phones">
      <li>
        <svg width="22" height="18" viewBox="0 0 22 18"><path d="M1 5c0-3 4-4 10-4s10 1 10 4v2h-5V5H6v2H1z"/><rect x="4" y="8" width="14" height="10" rx="2"/></svg>
        <span>714-555-0147</span>
      </li>
      <li>
        <svg width="22" height="20" viewBox="0 0 22 20"><rect x="6" y="0" width="10" height="20" rx="2"/><rect x="8" y="3" width="6" height="6" fill="#161616"/></svg>
        <span>714-555-0192</span>
      </li>
      <li>
        <svg width="22" height="20" viewBox="0 0 22 20"><rect x="5" y="0" width="12" height="7"/><rect x="1" y="7" width="20" height="13" rx="2"/><rect x="5" y="11" width="12" height="2" fill="#161616"/></svg>
        <span>714-555-0163</span>
      </li>
    </ul>

    <div class="watermark">
      <span class="word">BLUESTONE</span>
      <span class="tagline">ENGINEERING &amp; CONSTRUCTION INC.</span>
    </div>
  </section>

</body>
</html>
```